Business card design for new eCommerce site focusing on integrity and strong businsess tactics

We need a business card that will stand out and be memorable. Something with color that matches our company logo colors. Think high end version of Dealvine. There are 2 logos provided. The parent company is called Bright Harbor Ventures and we are presenting a new and very exciting eCommerce site called KeenTraders.example.

Target Market(s)

Our target markets are in the Activities, Food and Beverage, Health and Beauty

Industry/Entity Type

Marketing

Contact Information for Business Card

We have 4 members that need cards...I will provide all info to the winner of the design contest
Business Address is
48730 West 61st Avenue, Suite C204
Phoenix AZ 85917

Font styles to use
Serif
Sans Serif

Colors

Designer to choose colors to be used in the design.

Requirements
Must have
• The card must be memorable...should be unique in design but must exude integrity and be playful .
• I have provided several colors or our parent company...please feel free to use which ever
Nice to have
• I will leave this up to you. Feel free to use other images of your choosing that wraps around our client.....Activities, Dining, Health, Beauty
Should not have
• just dont be boring

```html
<!DOCTYPE html>
<html lang="en">
<head>
<meta charset="utf-8">
<title>Bright Harbor Ventures – Business Card</title>
<link href="https://fonts.googleapis.com/css2?family=Open+Sans:wght@400;600;700&display=swap" rel="stylesheet">
<style>
  :root {
    --navy: #111d4a;
    --navy-deep: #0c1638;
    --gold: #f2bd1d;
    --paper: #f4f4f4;
    --white: #ffffff;
    --backdrop: #d9d9d9;
  }
  html, body {
    margin: 0;
    width: 1200px;
    height: 904px;
    overflow: hidden;
    background: var(--backdrop);
    font-family: "Open Sans", sans-serif;
  }
  .sheet {
    position: relative;
    width: 1200px;
    height: 904px;
  }
  .card {
    position: absolute;
    left: 300px;
    width: 600px;
    height: 343px;
    box-shadow: 0 6px 18px rgba(0,0,0,0.18);
    overflow: hidden;
  }
  .card--back {
    top: 80px;
    background: var(--navy);
  }
  .card--front {
    top: 481px;
    background: var(--paper);
  }
  .brand-back {
    position: absolute;
    left: 0;
    right: 0;
    top: 150px;
    text-align: center;
    color: var(--white);
    font-weight: 700;
    font-size: 26px;
    letter-spacing: -0.3px;
  }
  .card-art {
    position: absolute;
    inset: 0;
  }
  .brand-front {
    position: absolute;
    left: 30px;
    width: 240px;
    top: 92px;
    text-align: center;
    color: var(--navy);
  }
  .brand-front__mark {
    width: 90px;
    height: 90px;
    margin: 0 auto 14px;
    border-radius: 50%;
    background: var(--navy);
  }
  .brand-front__name {
    font-weight: 700;
    font-size: 22px;
    line-height: 1.1;
    letter-spacing: -0.3px;
  }
  .contact {
    position: absolute;
    left: 390px;
    top: 62px;
    color: var(--white);
    font-size: 13px;
    line-height: 1.45;
  }
  .contact__name {
    color: var(--gold);
    font-weight: 700;
    font-size: 18px;
    line-height: 1.2;
  }
  .contact__title {
    margin-bottom: 14px;
  }
  .contact__address {
    margin: 0 0 12px;
    font-style: normal;
  }
  .contact__list {
    list-style: none;
    margin: 0;
    padding: 0;
  }
  .contact__list li {
    display: flex;
    align-items: center;
    gap: 9px;
  }
  .contact__icon {
    width: 12px;
    height: 12px;
    flex: none;
  }
</style>
</head>
<body>
<main class="sheet">
  <section class="card card--back" aria-label="Card back">
    <div class="brand-back">KeenTraders.example</div>
  </section>

  <section class="card card--front" aria-label="Card front">
    <svg class="card-art" viewBox="0 0 600 343" width="600" height="343" aria-hidden="true">
      <path d="M236,0 C318,62 356,200 348,343 L600,343 L600,0 Z" fill="var(--gold)"/>
      <path d="M252,0 C334,62 372,200 364,343 L600,343 L600,0 Z" fill="var(--navy)"/>
    </svg>

    <div class="brand-front">
      <div class="brand-front__mark"></div>
      <div class="brand-front__name">Bright Harbor Ventures</div>
    </div>

    <div class="contact">
      <div class="contact__name">Daniel Reyes</div>
      <div class="contact__title">Manager</div>
      <address class="contact__address">
        48730 West 61st Avenue<br>
        Suite C204<br>
        Phoenix AZ 85917
      </address>
      <ul class="contact__list">
        <li>
          <svg class="contact__icon" viewBox="0 0 12 12"><path d="M2.5 1 L4.5 1 L5.3 3.4 L4 4.4 C4.7 6 6 7.3 7.6 8 L8.6 6.7 L11 7.5 L11 9.5 C11 10.4 10.3 11 9.4 11 C5 10.7 1.3 7 1 2.6 C1 1.7 1.6 1 2.5 1 Z" fill="var(--gold)"/></svg>
          +1 555 014 2788
        </li>
        <li>
          <svg class="contact__icon" viewBox="0 0 12 12"><rect x="0.5" y="2.5" width="11" height="7.5" rx="1" fill="var(--gold)"/><path d="M1 3 L6 7 L11 3" fill="none" stroke="var(--navy)" stroke-width="1"/></svg>
          info@brightharbor.example
        </li>
        <li>
          <svg class="contact__icon" viewBox="0 0 12 12"><circle cx="6" cy="6" r="5.2" fill="none" stroke="var(--gold)" stroke-width="1.3"/><path d="M1 6 H11 M6 1 C3.5 4 3.5 8 6 11 M6 1 C8.5 4 8.5 8 6 11" fill="none" stroke="var(--gold)" stroke-width="1"/></svg>
          www.brightharbor.example
        </li>
      </ul>
    </div>
  </section>
</main>
</body>
</html>
```